Redesign Two Website Pages (Homepage & Features) — Modern, Responsive, and Visually Engaging

We’re looking to redesign two pages of our website:

Homepage: https://velmorak.com
Features Page: https://velmorak.com/features

We already have a preliminary design in Figma for the homepage, but it currently feels too plain. Please don’t use this Figma file provided. It was only shared for facilitate using the current website content and not as a source for inspiration. Use your creativity to bring something fresh and less dull as the current design.

We want to enhance it with visually engaging elements, such as illustrations, graphics, or images that align with the content and the application’s purpose, making the design more dynamic and marketing-oriented.

Requirements:
- Create modern, visually appealing designs for both pages.
- Include relevant visuals (images or vector graphics) that complement the content and improve user engagement.
- Ensure full responsiveness across all major viewports: desktop, tablet, and mobile.
- Deliver the final design in Figma format.
- You can choose any colour palette that best fits the concept, but please retain the existing content from the live website.
- We’re looking for a clean, modern, and commercially appealing design that effectively communicates the value of our product.

Target Market(s)

B2B

Number of Pages Required

2 page

Font styles to use
Sans Serif

Requirements
Must have
• Images and graphics to make the design and product more attractive.

```html
<!DOCTYPE html>
<html lang="en">
<head>
<meta charset="utf-8">
<title>Velmorak — Audit platform</title>
<link rel="stylesheet" href="https://fonts.googleapis.com/css2?family=Inter:wght@400;500;600;700;800&display=swap">
<style>
:root{
  --blue:#1a66d6;
  --blue-dark:#0f4fb8;
  --band:#1f5fd0;
  --ink:#111827;
  --muted:#5b6474;
  --soft:#eaf1fb;
  --line:#e3e8ef;
  --red:#d93a3a;
  --green:#1f9d57;
  --dark:#1c1f26;
  --white:#ffffff;
  --yellow:#f7c325;
}
*{box-sizing:border-box;margin:0;padding:0}
html,body{width:1200px;height:4815px;overflow:hidden}
body{font-family:"Inter",sans-serif;color:var(--ink);background:var(--white);position:relative}
section,header,footer{position:absolute;left:0;width:1200px}

/* Hero */
.hero{top:0;height:860px;background:linear-gradient(180deg,#dbe8f8 0%,#eef4fc 60%,#ffffff 100%)}
.nav{position:absolute;left:66px;top:46px;width:1068px;height:64px;background:var(--white);border-radius:6px;box-shadow:0 2px 10px rgba(20,50,110,.08);display:flex;align-items:center;padding:0 28px}
.brand{display:flex;align-items:center;gap:10px}
.brand-dot{width:26px;height:26px;border-radius:50%;background:var(--blue)}
.brand-name{font-weight:700;font-size:16px;color:var(--ink);line-height:1.1}
.brand-tag{font-size:11px;color:var(--muted)}
.nav-links{display:flex;gap:44px;margin-left:96px;font-size:13px;font-weight:500}
.nav-links a{color:var(--ink);text-decoration:none;position:relative}
.nav-links a.active:after{content:"";position:absolute;left:-8px;right:-8px;top:40px;height:3px;background:var(--blue)}
.nav-actions{margin-left:auto;display:flex;align-items:center;gap:18px;font-size:13px;font-weight:500}
.btn{display:inline-flex;align-items:center;justify-content:center;border-radius:4px;font-weight:600;font-size:13px;text-decoration:none}
.btn-primary{background:var(--blue);color:var(--white)}
.btn-ghost{background:var(--white);color:var(--ink);border:1px solid var(--line)}
.nav .btn-primary{height:34px;padding:0 16px;font-size:12px}
.hero-inner{position:absolute;top:180px;left:0;width:1200px;text-align:center}
.eyebrow{font-size:12px;font-weight:600;color:var(--blue)}
.hero h1{font-size:40px;font-weight:800;letter-spacing:-1px;line-height:1.25;margin-top:18px}
.hero h1 span{color:var(--blue);display:block}
.hero p.lead{font-size:13px;color:#3d4452;line-height:1.6;width:620px;margin:22px auto 0}
.hero-ctas{display:flex;gap:14px;justify-content:center;margin-top:24px}
.hero-ctas .btn{height:38px;padding:0 26px}
.hero .note{font-size:12px;color:#3d4452;margin-top:26px}
.stats{display:flex;justify-content:center;margin-top:40px}
.stat{width:164px;text-align:center;border-right:1px solid #c9d5e6}
.stat:last-child{border-right:0}
.stat b{display:block;font-size:20px;font-weight:700}
.stat small{font-size:10px;color:var(--muted)}
.saves{display:flex;align-items:center;justify-content:center;gap:12px;font-size:11px;color:#3d4452;margin-top:26px}
.saves i{width:18px;height:18px;border:2px solid var(--blue);border-radius:50%}
.pain-head{position:absolute;top:752px;width:1200px;text-align:center}
.pain-head h2{font-size:28px;font-weight:700;letter-spacing:-.3px}
.pain-head p{font-size:14px;color:var(--muted);margin-top:10px}

/* Problem band */
.compare{top:860px;height:460px}
.compare svg.wave{position:absolute;left:0;top:0}
.cmp-card{position:absolute;top:0;width:420px;height:236px;background:var(--white);border-radius:4px;box-shadow:0 6px 18px rgba(10,30,80,.15);padding:30px 28px}
.cmp-card.bad{left:168px;border-top:3px solid var(--red)}
.cmp-card.good{left:616px;border-top:3px solid var(--green)}
.cmp-card h3{font-size:17px;font-weight:600;margin-bottom:22px}
.bad h3{color:var(--red)} .good h3{color:var(--green)}
.cmp-card li{list-style:none;display:flex;align-items:center;gap:12px;font-size:12px;color:#333;margin-bottom:18px}
.mark{width:12px;height:12px;flex:none}

/* Features */
.features{top:1320px;height:600px;text-align:center}
.features h2{font-size:28px;font-weight:700;letter-spacing:-.3px}
.features > p{font-size:14px;color:var(--muted);margin-top:8px}
.feat-grid{display:grid;grid-template-columns:repeat(3,320px);column-gap:4px;row-gap:44px;justify-content:center;margin-top:44px;text-align:left}
.feat{padding:22px 24px 24px;display:flex;gap:16px}
.feat.focus{border-top:3px solid var(--blue);background:#f6f9fe;box-shadow:0 4px 16px rgba(20,60,140,.08)}
.feat-icon{width:20px;height:20px;flex:none;color:var(--blue)}
.feat h4{font-size:13px;font-weight:600}
.feat p{font-size:11px;color:var(--muted);line-height:1.55;margin-top:8px}
.pill{display:inline-block;background:var(--blue);color:var(--white);font-size:10px;font-weight:600;padding:4px 12px;border-radius:20px;margin-top:12px}

/* Testimonials */
.reviews{top:1940px;height:740px;background:linear-gradient(180deg,#eef4fc 0%,#f6f9fe 70%,#ffffff 100%);overflow:hidden;text-align:center}
.reviews h2{font-size:28px;font-weight:700;margin-top:76px;letter-spacing:-.3px}
.reviews > p{font-size:14px;color:var(--muted);margin-top:8px}
.review-row{position:absolute;display:flex;gap:32px;text-align:left}
.row-a{top:186px;left:-118px}
.row-b{top:426px;left:70px}
.review{width:330px;height:208px;background:var(--white);border-radius:4px;box-shadow:0 2px 10px rgba(20,50,110,.06);padding:22px 24px;flex:none}
.who{display:flex;align-items:center;gap:14px}
.avatar{width:48px;height:48px;border-radius:50%;background:linear-gradient(135deg,#8a6a58,#d6b49a);flex:none}
.who b{font-size:13px;font-weight:600;display:block}
.who small{font-size:11px;color:var(--muted)}
.review q{display:block;font-size:11px;color:#4a5160;line-height:1.6;margin-top:16px;quotes:"\201C" "\201D"}
.stars{color:#f5b301;font-size:14px;letter-spacing:2px;margin-top:10px}

/* Pricing */
.pricing{top:2680px;height:1240px;text-align:center}
.save-chip{display:inline-block;font-size:13px;font-weight:500;background:#eef3fb;border:1px solid #d2def0;padding:6px 14px;border-radius:20px;margin-top:20px}
.pricing h2{font-size:28px;font-weight:700;margin-top:26px;letter-spacing:-.3px}
.pricing > p{font-size:14px;color:var(--muted);margin-top:8px}
.toggle-wrap{display:flex;justify-content:center;align-items:center;gap:10px;margin-top:46px}
.off-tag{background:var(--dark);color:var(--white);font-size:14px;font-weight:600;padding:8px 14px;border-radius:3px}
.toggle{display:flex;background:#eef1f5;border-radius:24px;padding:4px;font-size:14px;font-weight:500}
.toggle span{padding:9px 20px;border-radius:20px}
.toggle .on{background:var(--blue);color:var(--white)}
.plans{position:absolute;left:150px;top:352px;width:900px}
.plans-frame{position:absolute;left:-2px;top:70px;width:1068px;height:700px;border:1px solid var(--line);border-radius:4px;transform:translateX(-82px)}
.plan-cols{position:absolute;left:-82px;top:70px;display:grid;grid-template-columns:repeat(4,266px);width:1068px}
.plan{padding:30px 26px;text-align:center;border-right:1px solid var(--line);height:700px}
.plan:last-child{border-right:0}
.plan h3{font-size:17px;font-weight:600}
.plan .desc{font-size:10px;color:var(--muted);line-height:1.5;margin:14px auto 0;width:190px}
.price{font-size:38px;font-weight:700;margin-top:16px;letter-spacing:-1px}
.price small{font-size:12px;font-weight:400;letter-spacing:0}
.per{font-size:12px;color:#333;margin-top:4px}
.per em{font-style:normal;font-size:9px;color:var(--red);border:1px solid var(--red);border-radius:10px;padding:1px 6px;margin-left:4px}
.plan .btn{width:160px;height:32px;font-size:11px;margin-top:10px}
.plan ul{list-style:none;text-align:left;margin-top:22px}
.plan li{display:flex;align-items:flex-start;gap:10px;font-size:11px;color:#2a2f38;margin-bottom:15px;line-height:1.4}
.ck{width:15px;height:15px;flex:none}
.plan.pro{background:var(--dark);color:var(--white);margin-top:-52px;height:820px;border-radius:4px;border:0;position:relative}
.pro .badge{position:absolute;top:-14px;left:50%;transform:translateX(-50%);background:var(--yellow);color:var(--ink);font-size:10px;font-weight:600;padding:6px 16px;border-radius:12px}
.pro h3{margin-top:20px}
.pro .desc,.pro .per,.pro li{color:#e8eaee}
.pro .per em{color:#e8eaee;border-color:#e8eaee}
.pro .btn{width:180px}
.pro li{margin-bottom:18px}

/* CTA */
.cta{top:3930px;height:400px}
.cta-box{position:absolute;left:70px;top:0;width:1062px;height:340px;background:var(--blue);border-radius:4px;overflow:hidden}
.cta-sun{position:absolute;left:170px;top:-120px;width:190px;height:190px;border-radius:50%;background:var(--yellow)}
.cta-art{position:absolute;right:70px;bottom:0;width:320px;height:330px;border-radius:160px 160px 0 0;background:linear-gradient(180deg,#2a78e6,#0f4fb8)}
.cta h2{position:absolute;left:70px;top:110px;font-size:28px;font-weight:600;color:var(--white)}
.cta p{position:absolute;left:70px;top:156px;font-size:14px;color:#dbe7fb}
.cta-actions{position:absolute;left:68px;top:206px;display:flex;gap:10px}
.cta-actions .btn{height:40px;padding:0 26px;font-size:13px;font-weight:500}
.btn-white{background:var(--white);color:var(--ink);gap:14px}
.btn-outline{border:1px solid var(--white);color:var(--white)}

/* Footer */
.footer{top:4330px;height:485px;background:linear-gradient(180deg,#ffffff 0%,#e4edf9 100%)}
.footer .brand{position:absolute;left:70px;top:56px}
.fcol{position:absolute;top:56px}
.fcol h5{font-size:17px;font-weight:500;margin-bottom:34px}
.fcol a{display:block;font-size:12px;color:#3d4452;text-decoration:none;margin-bottom:26px}
.fcol a:before{content:"» ";color:#8a93a3}
.chat{position:absolute;right:66px;top:330px;width:44px;height:44px;border-radius:50%;background:var(--blue);display:flex;align-items:center;justify-content:center}
.legal-bar{position:absolute;left:0;bottom:0;width:1200px;height:38px;background:#1d1f24;color:#d8dbe0;font-size:10px;display:flex;align-items:center;justify-content:center}
</style>
</head>
<body>

<header class="hero">
  <nav class="nav">
    <div class="brand">
      <span class="brand-dot"></span>
      <div><div class="brand-name">Velmorak</div><div class="brand-tag">Guiding every audit with clarity</div></div>
    </div>
    <div class="nav-links">
      <a class="active" href="https://velmorak.com">Home</a>
      <a href="https://velmorak.com/features">Features</a>
      <a href="#pricing">Pricing</a>
      <a href="#demo">Demo</a>
    </div>
    <div class="nav-actions">
      <span>Sign up</span>
      <a class="btn btn-primary" href="#signin">Sign in</a>
    </div>
  </nav>

  <div class="hero-inner">
    <div class="eyebrow">Trusted by 300+ audit firms worldwide</div>
    <h1>Cut audit time by 60%<span>without cutting corners</span></h1>
    <p class="lead">The only audit platform that combines AI-powered template generation, real-time collaboration, and intelligent compliance tracking. Join leading firms completing audits 3x faster with 99.9% accuracy.</p>
    <div class="hero-ctas">
      <a class="btn btn-primary" href="#trial">Start 14-day free trial</a>
      <a class="btn btn-ghost" href="#demo">Schedule demo</a>
    </div>
    <div class="note">No credit card required • 14-day free trial • Cancel anytime</div>
    <div class="stats">
      <div class="stat"><b>300+</b><small>Audit firms</small></div>
      <div class="stat"><b>1000+</b><small>Audits completed</small></div>
      <div class="stat"><b>99.9%</b><small>Compliance rate</small></div>
      <div class="stat"><b>4.9/5</b><small>Customer rating</small></div>
    </div>
    <div class="saves"><i></i>Average team saves 5–10 hrs/week</div>
  </div>

  <div class="pain-head">
    <h2>Stop losing $50K+ per year on manual Audits</h2>
    <p>Your team spends 70% of audit time on repetitive tasks. We fix that.</p>
  </div>
</header>

<section class="compare">
  <svg class="wave" width="1200" height="420" viewBox="0 0 1200 420" aria-hidden="true">
    <path d="M0 10 Q600 150 1200 10 L1200 400 Q600 300 0 400 Z" fill="var(--band)"/>
  </svg>
  <div class="cmp-card bad">
    <h3>Without Velmorak</h3>
    <ul>
      <li><svg class="mark" viewBox="0 0 12 12"><circle cx="6" cy="6" r="6" fill="#fde3e3"/><path d="M4 4l4 4M8 4l-4 4" stroke="#d93a3a" stroke-width="1.5"/></svg>200+ hours creating templates from scratch</li>
      <li><svg class="mark" viewBox="0 0 12 12"><circle cx="6" cy="6" r="6" fill="#fde3e3"/><path d="M4 4l4 4M8 4l-4 4" stroke="#d93a3a" stroke-width="1.5"/></svg>Version control chaos with Gridwell spreadsheets</li>
      <li><svg class="mark" viewBox="0 0 12 12"><circle cx="6" cy="6" r="6" fill="#fde3e3"/><path d="M4 4l4 4M8 4l-4 4" stroke="#d93a3a" stroke-width="1.5"/></svg>60% error rate from manual data entry</li>
      <li><svg class="mark" viewBox="0 0 12 12"><circle cx="6" cy="6" r="6" fill="#fde3e3"/><path d="M4 4l4 4M8 4l-4 4" stroke="#d93a3a" stroke-width="1.5"/></svg>Compliance violations risk $100K+ fines</li>
    </ul>
  </div>
  <div class="cmp-card good">
    <h3>With Velmorak</h3>
    <ul>
      <li><svg class="mark" viewBox="0 0 12 12"><circle cx="6" cy="6" r="6" fill="#dcf3e6"/><path d="M3.5 6.2l1.8 1.8 3.3-3.6" stroke="#1f9d57" stroke-width="1.5" fill="none"/></svg>AI generates templates in 30 seconds</li>
      <li><svg class="mark" viewBox="0 0 12 12"><circle cx="6" cy="6" r="6" fill="#dcf3e6"/><path d="M3.5 6.2l1.8 1.8 3.3-3.6" stroke="#1f9d57" stroke-width="1.5" fill="none"/></svg>Real-time collaboration with audit trail</li>
      <li><svg class="mark" viewBox="0 0 12 12"><circle cx="6" cy="6" r="6" fill="#dcf3e6"/><path d="M3.5 6.2l1.8 1.8 3.3-3.6" stroke="#1f9d57" stroke-width="1.5" fill="none"/></svg>Automated validation catches 99% of errors</li>
      <li><svg class="mark" viewBox="0 0 12 12"><circle cx="6" cy="6" r="6" fill="#dcf3e6"/><path d="M3.5 6.2l1.8 1.8 3.3-3.6" stroke="#1f9d57" stroke-width="1.5" fill="none"/></svg>Built-in compliance for ISO, GDPR, PCI DSS</li>
    </ul>
  </div>
</section>

<section class="features">
  <h2>Everything you need to scale your Audit practice</h2>
  <p>From solo practitioners to Big 4 firms, we've built the features that matter.</p>
  <div class="feat-grid">
    <div class="feat">
      <svg class="feat-icon" viewBox="0 0 20 20" fill="currentColor"><path d="M7 2l1.4 3.6L12 7l-3.6 1.4L7 12 5.6 8.4 2 7l3.6-1.4zM14 10l.9 2.1L17 13l-2.1.9L14 16l-.9-2.1L11 13l2.1-.9z"/></svg>
      <div><h4>AI-powered templates</h4><p>Generate industry-specific audit templates in 30 seconds. Our AI knows ISO 27001, GDPR, PCI DSS, and 50+ frameworks.</p><span class="pill">Save 200+ hours per year</span></div>
    </div>
    <div class="feat focus">
      <svg class="feat-icon" viewBox="0 0 20 20" fill="none" stroke="currentColor" stroke-width="1.6"><circle cx="7" cy="7" r="3"/><circle cx="14" cy="8" r="2.3"/><path d="M2 17c0-3 2.2-5 5-5s5 2 5 5M12 13c3 0 5 1.5 5 4"/></svg>
      <div><h4>Real-time collaboration</h4><p>Your entire team works together seamlessly. See changes instantly, leave comments, and track who did what.</p><span class="pill">3x faster team audits</span></div>
    </div>
    <div class="feat">
      <svg class="feat-icon" viewBox="0 0 20 20" fill="none" stroke="currentColor" stroke-width="1.6"><path d="M10 2l6 2.5v5c0 4-2.7 6.8-6 8.5-3.3-1.7-6-4.5-6-8.5v-5z"/></svg>
      <div><h4>Evidence management</h4><p>Attach documents, screenshots, and recordings directly to audit items. Never lose critical evidence again.</p><span class="pill">100% audit trail coverage</span></div>
    </div>
    <div class="feat">
      <svg class="feat-icon" viewBox="0 0 20 20" fill="none" stroke="currentColor" stroke-width="1.6"><path d="M2 5l1.5 1.5L6 4M2 12l1.5 1.5L6 11M9 5.5h9M9 12.5h9"/></svg>
      <div><h4>Automated workflows</h4><p>Set up once, run forever. Automated reminders, status updates, and report generation keep projects on track.</p><span class="pill">Zero missed deadlines</span></div>
    </div>
    <div class="feat">
      <svg class="feat-icon" viewBox="0 0 20 20" fill="none" stroke="currentColor" stroke-width="1.6"><path d="M2 2v16h16M5 13l4-4 3 3 5-6"/></svg>
      <div><h4>Smart analytics</h4><p>Spot risks before they become issues. Our dashboard shows completion rates, bottlenecks, and compliance gaps.</p><span class="pill">60% fewer compliance issues</span></div>
    </div>
    <div class="feat">
      <svg class="feat-icon" viewBox="0 0 20 20" fill="none" stroke="currentColor" stroke-width="1.6"><rect x="4" y="9" width="12" height="9" rx="1.5"/><path d="M6.5 9V6.5a3.5 3.5 0 017 0V9"/></svg>
      <div><h4>Bank-grade security</h4><p>End-to-end encryption, role-based access, and complete audit logs protect your data.</p><span class="pill">Zero security breaches</span></div>
    </div>
  </div>
</section>

<section class="reviews">
  <h2>Audit leaders choose Velmorak</h2>
  <p>See why we're rated 4.9/5 by 500+ audit professionals.</p>
  <div class="review-row row-a">
    <div class="review"><div class="who"><div class="avatar" role="img" aria-label="Portrait photo of the reviewer"></div><div><b>Mira Talbot</b><small>Partner, Harlow &amp; Pike CPA</small></div></div><q>We've reduced audit completion time from 3 weeks to 1 week. The AI templates alone saved us $200K in the first year. This is a game-changer for mid-size firms.</q><div class="stars">★★★★★</div></div>
    <div class="review"><div class="who"><div class="avatar" role="img" aria-label="Portrait photo of the reviewer"></div><div><b>Mira Talbot</b><small>Partner, Harlow &amp; Pike CPA</small></div></div><q>We've reduced audit completion time from 3 weeks to 1 week. The AI templates alone saved us $200K in the first year. This is a game-changer for mid-size firms.</q><div class="stars">★★★★★</div></div>
    <div class="review"><div class="who"><div class="avatar" role="img" aria-label="Portrait photo of the reviewer"></div><div><b>Mira Talbot</b><small>Partner, Harlow &amp; Pike CPA</small></div></div><q>We've reduced audit completion time from 3 weeks to 1 week. The AI templates alone saved us $200K in the first year. This is a game-changer for mid-size firms.</q><div class="stars">★★★★★</div></div>
    <div class="review"><div class="who"><div class="avatar" role="img" aria-label="Portrait photo of the reviewer"></div><div><b>Mira Talbot</b><small>Partner, Harlow &amp; Pike CPA</small></div></div><q>We've reduced audit completion time from 3 weeks to 1 week. The AI templates alone saved us $200K in the first year. This is a game-changer for mid-size firms.</q><div class="stars">★★★★★</div></div>
  </div>
  <div class="review-row row-b">
    <div class="review"><div class="who"><div class="avatar" role="img" aria-label="Portrait photo of the reviewer"></div><div><b>Mira Talbot</b><small>Partner, Harlow &amp; Pike CPA</small></div></div><q>We've reduced audit completion time from 3 weeks to 1 week. The AI templates alone saved us $200K in the first year. This is a game-changer for mid-size firms.</q><div class="stars">★★★★★</div></div>
    <div class="review"><div class="who"><div class="avatar" role="img" aria-label="Portrait photo of the reviewer"></div><div><b>Mira Talbot</b><small>Partner, Harlow &amp; Pike CPA</small></div></div><q>We've reduced audit completion time from 3 weeks to 1 week. The AI templates alone saved us $200K in the first year. This is a game-changer for mid-size firms.</q><div class="stars">★★★★★</div></div>
    <div class="review"><div class="who"><div class="avatar" role="img" aria-label="Portrait photo of the reviewer"></div><div><b>Mira Talbot</b><small>Partner, Harlow &amp; Pike CPA</small></div></div><q>We've reduced audit completion time from 3 weeks to 1 week. The AI templates alone saved us $200K in the first year. This is a game-changer for mid-size firms.</q><div class="stars">★★★★★</div></div>
    <div class="review"><div class="who"><div class="avatar" role="img" aria-label="Portrait photo of the reviewer"></div><div><b>Mira Talbot</b><small>Partner, Harlow &amp; Pike CPA</small></div></div><q>We've reduced audit completion time from 3 weeks to 1 week. The AI templates alone saved us $200K in the first year. This is a game-changer for mid-size firms.</q><div class="stars">★★★★★</div></div>
  </div>
</section>

<section class="pricing" id="pricing">
  <div class="save-chip">+ Save 21% with annual billing +</div>
  <h2>Simple Pricing That Scales With You</h2>
  <p>Choose the perfect plan for your audit team. All plans include a 14-day free trial.</p>
  <div class="toggle-wrap">
    <span class="off-tag">21% Off</span>
    <div class="toggle"><span>Monthly</span><span class="on">Yearly</span></div>
  </div>

  <div class="plans">
    <div class="plans-frame"></div>
    <div class="plan-cols">
      <div class="plan">
        <h3>Free plan</h3>
        <div class="desc">Perfect for getting started with basic auditing needs.</div>
        <div class="price">$0<small>/month</small></div>
        <div class="per">Up to 2 team members</div>
        <a class="btn btn-primary" href="#free">Get started for free</a>
        <ul>
          <li><svg class="ck" viewBox="0 0 15 15"><circle cx="7.5" cy="7.5" r="7.5" fill="#1f9d57"/><path d="M4.3 7.7l2.2 2.2 4.2-4.4" stroke="#fff" stroke-width="1.6" fill="none"/></svg>2 team members</li>
          <li><svg class="ck" viewBox="0 0 15 15"><circle cx="7.5" cy="7.5" r="7.5" fill="#1f9d57"/><path d="M4.3 7.7l2.2 2.2 4.2-4.4" stroke="#fff" stroke-width="1.6" fill="none"/></svg>5 templates</li>
          <li><svg class="ck" viewBox="0 0 15 15"><circle cx="7.5" cy="7.5" r="7.5" fill="#1f9d57"/><path d="M4.3 7.7l2.2 2.2 4.2-4.4" stroke="#fff" stroke-width="1.6" fill="none"/></svg>10 active projects</li>
          <li><svg class="ck" viewBox="0 0 15 15"><circle cx="7.5" cy="7.5" r="7.5" fill="#1f9d57"/><path d="M4.3 7.7l2.2 2.2 4.2-4.4" stroke="#fff" stroke-width="1.6" fill="none"/></svg>Evidence management</li>
          <li><svg class="ck" viewBox="0 0 15 15"><circle cx="7.5" cy="7.5" r="7.5" fill="#1f9d57"/><path d="M4.3 7.7l2.2 2.2 4.2-4.4" stroke="#fff" stroke-width="1.6" fill="none"/></svg>Basic support</li>
          <li><svg class="ck" viewBox="0 0 15 15"><circle cx="7.5" cy="7.5" r="7.5" fill="#1c1f26"/><path d="M5 5l5 5M10 5l-5 5" stroke="#fff" stroke-width="1.5"/></svg>Custom templates</li>
          <li><svg class="ck" viewBox="0 0 15 15"><circle cx="7.5" cy="7.5" r="7.5" fill="#1c1f26"/><path d="M5 5l5 5M10 5l-5 5" stroke="#fff" stroke-width="1.5"/></svg>Advanced analytics</li>
          <li><svg class="ck" viewBox="0 0 15 15"><circle cx="7.5" cy="7.5" r="7.5" fill="#1c1f26"/><path d="M5 5l5 5M10 5l-5 5" stroke="#fff" stroke-width="1.5"/></svg>Priority support</li>
        </ul>
      </div>
      <div class="plan">
        <h3>Starter</h3>
        <div class="desc">Perfect for small audit teams and solo practitioners.</div>
        <div class="price">$15<small>/month</small></div>
        <div class="per">$15/user x 1 user <em>21% off</em></div>
        <a class="btn btn-primary" href="#starter">Start free trail</a>
        <ul>
          <li><svg class="ck" viewBox="0 0 15 15"><circle cx="7.5" cy="7.5" r="7.5" fill="#1f9d57"/><path d="M4.3 7.7l2.2 2.2 4.2-4.4" stroke="#fff" stroke-width="1.6" fill="none"/></svg>Unlimited team members</li>
          <li><svg class="ck" viewBox="0 0 15 15"><circle cx="7.5" cy="7.5" r="7.5" fill="#1f9d57"/><path d="M4.3 7.7l2.2 2.2 4.2-4.4" stroke="#fff" stroke-width="1.6" fill="none"/></svg>10 active audits</li>
          <li><svg class="ck" viewBox="0 0 15 15"><circle cx="7.5" cy="7.5" r="7.5" fill="#1f9d57"/><path d="M4.3 7.7l2.2 2.2 4.2-4.4" stroke="#fff" stroke-width="1.6" fill="none"/></svg>Evidence management</li>
          <li><svg class="ck" viewBox="0 0 15 15"><circle cx="7.5" cy="7.5" r="7.5" fill="#1f9d57"/><path d="M4.3 7.7l2.2 2.2 4.2-4.4" stroke="#fff" stroke-width="1.6" fill="none"/></svg>Basic support</li>
          <li><svg class="ck" viewBox="0 0 15 15"><circle cx="7.5" cy="7.5" r="7.5" fill="#1f9d57"/><path d="M4.3 7.7l2.2 2.2 4.2-4.4" stroke="#fff" stroke-width="1.6" fill="none"/></svg>Email support</li>
          <li><svg class="ck" viewBox="0 0 15 15"><circle cx="7.5" cy="7.5" r="7.5" fill="#1c1f26"/><path d="M5 5l5 5M10 5l-5 5" stroke="#fff" stroke-width="1.5"/></svg>Custom workflows</li>
          <li><svg class="ck" viewBox="0 0 15 15"><circle cx="7.5" cy="7.5" r="7.5" fill="#1c1f26"/><path d="M5 5l5 5M10 5l-5 5" stroke="#fff" stroke-width="1.5"/></svg>Advanced analytics</li>
          <li><svg class="ck" viewBox="0 0 15 15"><circle cx="7.5" cy="7.5" r="7.5" fill="#1c1f26"/><path d="M5 5l5 5M10 5l-5 5" stroke="#fff" stroke-width="1.5"/></svg>Dedicated account manager</li>
        </ul>
      </div>
      <div class="plan pro">
        <span class="badge">Most popular</span>
        <h3>Professional</h3>
        <div class="desc">Ideal for growing audit firms with multiple clients.</div>
        <div class="price">$39<small>/month</small></div>
        <div class="per">$39/user x 1 user <em>21% off</em></div>
        <a class="btn btn-primary" href="#pro">Start free trail</a>
        <ul>
          <li><svg class="ck" viewBox="0 0 15 15"><circle cx="7.5" cy="7.5" r="7.5" fill="#1f9d57"/><path d="M4.3 7.7l2.2 2.2 4.2-4.4" stroke="#fff" stroke-width="1.6" fill="none"/></svg>Unlimited team members</li>
          <li><svg class="ck" viewBox="0 0 15 15"><circle cx="7.5" cy="7.5" r="7.5" fill="#1f9d57"/><path d="M4.3 7.7l2.2 2.2 4.2-4.4" stroke="#fff" stroke-width="1.6" fill="none"/></svg>Unlimited audits</li>
          <li><svg class="ck" viewBox="0 0 15 15"><circle cx="7.5" cy="7.5" r="7.5" fill="#1f9d57"/><path d="M4.3 7.7l2.2 2.2 4.2-4.4" stroke="#fff" stroke-width="1.6" fill="none"/></svg>Custom templates + AI builder</li>
          <li><svg class="ck" viewBox="0 0 15 15"><circle cx="7.5" cy="7.5" r="7.5" fill="#1f9d57"/><path d="M4.3 7.7l2.2 2.2 4.2-4.4" stroke="#fff" stroke-width="1.6" fill="none"/></svg>Evidence management</li>
          <li><svg class="ck" viewBox="0 0 15 15"><circle cx="7.5" cy="7.5" r="7.5" fill="#1f9d57"/><path d="M4.3 7.7l2.2 2.2 4.2-4.4" stroke="#fff" stroke-width="1.6" fill="none"/></svg>Templates library</li>
          <li><svg class="ck" viewBox="0 0 15 15"><circle cx="7.5" cy="7.5" r="7.5" fill="#1f9d57"/><path d="M4.3 7.7l2.2 2.2 4.2-4.4" stroke="#fff" stroke-width="1.6" fill="none"/></svg>Advanced evidence management</li>
          <li><svg class="ck" viewBox="0 0 15 15"><circle cx="7.5" cy="7.5" r="7.5" fill="#1f9d57"/><path d="M4.3 7.7l2.2 2.2 4.2-4.4" stroke="#fff" stroke-width="1.6" fill="none"/></svg>AI-powered scoring analysis</li>
          <li><svg class="ck" viewBox="0 0 15 15"><circle cx="7.5" cy="7.5" r="7.5" fill="#1f9d57"/><path d="M4.3 7.7l2.2 2.2 4.2-4.4" stroke="#fff" stroke-width="1.6" fill="none"/></svg>Priority support</li>
          <li><svg class="ck" viewBox="0 0 15 15"><circle cx="7.5" cy="7.5" r="7.5" fill="#1f9d57"/><path d="M4.3 7.7l2.2 2.2 4.2-4.4" stroke="#fff" stroke-width="1.6" fill="none"/></svg>Custom workflows</li>
          <li><svg class="ck" viewBox="0 0 15 15"><circle cx="7.5" cy="7.5" r="7.5" fill="#1f9d57"/><path d="M4.3 7.7l2.2 2.2 4.2-4.4" stroke="#fff" stroke-width="1.6" fill="none"/></svg>Advanced analytics</li>
          <li><svg class="ck" viewBox="0 0 15 15"><circle cx="7.5" cy="7.5" r="7.5" fill="#1f9d57"/><path d="M4.3 7.7l2.2 2.2 4.2-4.4" stroke="#fff" stroke-width="1.6" fill="none"/></svg>PII detection</li>
          <li><svg class="ck" viewBox="0 0 15 15"><circle cx="7.5" cy="7.5" r="7" fill="none" stroke="#fff"/><path d="M5 5l5 5M10 5l-5 5" stroke="#fff" stroke-width="1.5"/></svg>Dedicated account manager</li>
        </ul>
      </div>
      <div class="plan">
        <h3>Free plan</h3>
        <div class="desc">Perfect for getting started with basic auditing needs.</div>
        <div class="price">$0<small>/month</small></div>
        <div class="per">Up to 2 team members</div>
        <a class="btn btn-primary" href="#free">Get started for free</a>
        <ul>
          <li><svg class="ck" viewBox="0 0 15 15"><circle cx="7.5" cy="7.5" r="7.5" fill="#1f9d57"/><path d="M4.3 7.7l2.2 2.2 4.2-4.4" stroke="#fff" stroke-width="1.6" fill="none"/></svg>Unlimited team members</li>
          <li><svg class="ck" viewBox="0 0 15 15"><circle cx="7.5" cy="7.5" r="7.5" fill="#1f9d57"/><path d="M4.3 7.7l2.2 2.2 4.2-4.4" stroke="#fff" stroke-width="1.6" fill="none"/></svg>Unlimited audits</li>
          <li><svg class="ck" viewBox="0 0 15 15"><circle cx="7.5" cy="7.5" r="7.5" fill="#1f9d57"/><path d="M4.3 7.7l2.2 2.2 4.2-4.4" stroke="#fff" stroke-width="1.6" fill="none"/></svg>All features included</li>
          <li><svg class="ck" viewBox="0 0 15 15"><circle cx="7.5" cy="7.5" r="7.5" fill="#1f9d57"/><path d="M4.3 7.7l2.2 2.2 4.2-4.4" stroke="#fff" stroke-width="1.6" fill="none"/></svg>Templates library</li>
          <li><svg class="ck" viewBox="0 0 15 15"><circle cx="7.5" cy="7.5" r="7.5" fill="#1f9d57"/><path d="M4.3 7.7l2.2 2.2 4.2-4.4" stroke="#fff" stroke-width="1.6" fill="none"/></svg>AI-powered scoring analysis</li>
          <li><svg class="ck" viewBox="0 0 15 15"><circle cx="7.5" cy="7.5" r="7.5" fill="#1f9d57"/><path d="M4.3 7.7l2.2 2.2 4.2-4.4" stroke="#fff" stroke-width="1.6" fill="none"/></svg>Enterprise security</li>
          <li><svg class="ck" viewBox="0 0 15 15"><circle cx="7.5" cy="7.5" r="7.5" fill="#1f9d57"/><path d="M4.3 7.7l2.2 2.2 4.2-4.4" stroke="#fff" stroke-width="1.6" fill="none"/></svg>Regional compliance</li>
          <li><svg class="ck" viewBox="0 0 15 15"><circle cx="7.5" cy="7.5" r="7.5" fill="#1f9d57"/><path d="M4.3 7.7l2.2 2.2 4.2-4.4" stroke="#fff" stroke-width="1.6" fill="none"/></svg>Data residency guaranteed</li>
          <li><svg class="ck" viewBox="0 0 15 15"><circle cx="7.5" cy="7.5" r="7.5" fill="#1f9d57"/><path d="M4.3 7.7l2.2 2.2 4.2-4.4" stroke="#fff" stroke-width="1.6" fill="none"/></svg>Custom workflows</li>
          <li><svg class="ck" viewBox="0 0 15 15"><circle cx="7.5" cy="7.5" r="7.5" fill="#1f9d57"/><path d="M4.3 7.7l2.2 2.2 4.2-4.4" stroke="#fff" stroke-width="1.6" fill="none"/></svg>Advanced analytics</li>
          <li><svg class="ck" viewBox="0 0 15 15"><circle cx="7.5" cy="7.5" r="7.5" fill="#1f9d57"/><path d="M4.3 7.7l2.2 2.2 4.2-4.4" stroke="#fff" stroke-width="1.6" fill="none"/></svg>PII detection</li>
          <li><svg class="ck" viewBox="0 0 15 15"><circle cx="7.5" cy="7.5" r="7.5" fill="#1f9d57"/><path d="M4.3 7.7l2.2 2.2 4.2-4.4" stroke="#fff" stroke-width="1.6" fill="none"/></svg>Dedicated account manager</li>
        </ul>
      </div>
    </div>
  </div>
</section>

<section class="cta" id="demo">
  <div class="cta-box">
    <div class="cta-sun"></div>
    <div class="cta-art" role="img" aria-label="Illustration of a smiling woman pointing toward the call to action"></div>
    <h2>Ready to Transform Your Audits?</h2>
    <p>Join hundreds of companies saving time and money with Velmorak</p>
    <div class="cta-actions">
      <a class="btn btn-white" href="#trial">Start Free Trial <svg width="14" height="10" viewBox="0 0 14 10"><path d="M1 5h11M8 1l4 4-4 4" stroke="#111827" stroke-width="1.6" fill="none"/></svg></a>
      <a class="btn btn-outline" href="#demo">Schedule Demo</a>
    </div>
  </div>
</section>

<footer class="footer">
  <div class="brand">
    <span class="brand-dot"></span>
    <div><div class="brand-name">Velmorak</div><div class="brand-tag">Guiding every audit with clarity</div></div>
  </div>
  <div class="fcol" style="left:500px"><h5>Product</h5><a href="https://velmorak.com/features">Features</a><a href="#pricing">Pricing</a><a href="#demo">Demo</a><a href="#signin">Sign in</a></div>
  <div class="fcol" style="left:728px"><h5>Company</h5><a href="#about">About</a><a href="#contact">Contact</a><a href="#status">System status</a></div>
  <div class="fcol" style="left:986px"><h5>Legal</h5><a href="#privacy">Privacy policy</a><a href="#terms">Terms of service</a><a href="#security">Security</a><a href="#compliance">Compliance</a></div>
  <div class="chat"><svg width="20" height="18" viewBox="0 0 20 18"><path d="M2 2h16v10H8l-4 4v-4H2z" fill="none" stroke="#fff" stroke-width="1.6"/></svg></div>
  <div class="legal-bar">© 2025 Brennix Labs Velmorak &nbsp;| All Rights Reserved</div>
</footer>

</body>
</html>
```